依頼詳細
かなり豪華な(市販価格1,890円)フルカラーのカタログを自社製作しており、
それをホームページ上で無料でプレゼントしています。
現在はこのようなページになっています。
http://www.tomosa-atelier.com/contact/
いろいろな資料が同時に請求できるようになっていますが、
今回依頼したいのは、施工事例カタログ専用のランディングページです。

イメージは、森市のヒット商品の販売ページみたいな感じです。
(安っぽいデザインのページが多いので、もっと高級感を出したいですが)
こちらのサイトでいろいろ作例が載っていました。
http://www.kanaho-works.jp/theme18.html

こんな感じも好きです。
http://burotake.co.jp/recruit/legend-designer/

1ページの構成にしたいですが、
あまりタテに長く作りたくありません。
モニター2画面分くらいで収めたいです。

カタログの特徴はこちらです。
■フルカラー・300ページ。
■エクステリアの施工例に特化したカタログは希少。
■価格が載っているので、自宅を工事する場合の金額のイメージが付けやすい。
■定価1890円でソルテで販売中のものが無料でもらえる。

サイトURL
http://www.tomosa-atelier.com/
ページ数
1ページ
希望イメージ
シンプル 複雑
単色 カラフル
暗い 明るい
日常 高級
遊び心 厳粛
未来的 伝統的
女性的 男性的
希望する色
グリーン・ベージュ・ブラウン・ブラック
納品ファイル
• 高解像度JPG (.jpg)
• イラストレーター形式 (.ai)
補足説明
古いカタログの画像ですが、製作用の参考に添付しておきます。
http://filebasket.example/download/5c1e2f7a9d03b46e8a7c21f0d5b9e3a4c6f81d27

画像等の素材もアップしました。
http://filebasket.example/download/7e2a9c05b1d84f36a0c7e95b2d1f48a6c3e07b92
http://filebasket.example/download/b41d8e27c6a05f93e1b7d24a8c0f65e9d3a17c58

ご提案の際はダミーのカタログ画像などで行っていただき、
当選の方には実際のカタログをご送付し、最終的に仕上げていただきます。
締め切りを2日延長しました。
よろしくお願いします。
訴求のポイントについてご質問いただきましたので、
一つ付け加えたいと思います。

「制作費が非常に高いため、在庫が無くなり次第終了です」
というような言葉をつかっていただけますか?
※言い方はこの通りでなくてもOKです。

今回のページはリスティング広告用のランディングページになりますので、資料請求(=カタログの無料プレゼントへの申し込み)をしてもらうことが最大の目的です。そのためには、無料であること、豪華なこと、内容が濃いことなどを訴求していただければと思います。

よろしくお願いします。
報酬をアップしました。
よろしくお願いします。
>1ページの構成にしたいですが、
>あまりタテに長く作りたくありません。
>モニター2画面分くらいで収めたいです。

依頼内容にこのように記載しましたが、
これは無視していただいてかまいません。
※どれだけタテに長くなってもOKです。
ご提案ありがとうございます。
一つ注意点があります。
サイト訪問者に動作をしてもらうようなページはNGでお願いします。
(クリックしてページをめくるなど)
動作に凝らなくい方がいいですし、ビジュアルも然りです。
単純にこの一覧のようなページでかまいません。
http://www.pagegallery-hub.jp/
よろしくお願いします。
素材のアップロード期限が過ぎてしまったため、
こちらに再アップしました。

http://filebasket.example/download/9f05c3b8e1a27d64c8b0f3e5a91d7c26e4b08f13

http://filebasket.example/download/2c8e6a1f0d47b95e3a2c18d7f6b0e94a5d31c7b6

http://filebasket.example/download/e6b37d0a94c2f815d7e0a6b3c29f48d1a75e0c39

よろしくお願いします。

デザインの第一印象がとてもよく、コンテンツも見やすくまとまっており、高いコンバージョンが期待できる作品だと思いました。

魅力的なご提案をありがとうございました。
こういったデザインコンペは今後も複数依頼予定ですので、次回もよろしくお願いします。

```html
<!DOCTYPE html>
<html lang="ja">
<head>
<meta charset="utf-8">
<title>施工事例カタログ 数量限定プレゼント | 灯砂ガーデン</title>
<link rel="stylesheet" href="https://fonts.googleapis.com/css2?family=Noto+Serif+JP:wght@400;600;700&family=Noto+Sans+JP:wght@400;500;700&family=Oswald:wght@500&display=swap">
<style>
:root{
  --bg:#e8e5df;
  --paper:#f8f6f1;
  --ink:#2b2622;
  --ink-soft:#6a625a;
  --orange:#e8762b;
  --band:#2a2623;
  --band-low:#4a4541;
  --green:#5c7a3a;
  --stone:#b9ad9b;
  --leaf:#7d8f5e;
  --wood:#8a6a4c;
  --link:#3a5a8a;
  --white:#ffffff;
}
*{box-sizing:border-box;margin:0;padding:0}
html,body{width:680px;height:1200px;overflow:hidden}
body{background:var(--bg);font-family:"Noto Sans JP",sans-serif;color:var(--ink);position:relative}
.abs{position:absolute}

/* catalog spread */
.spread{left:14px;top:0;width:656px;height:884px;background:var(--paper);box-shadow:0 6px 14px rgba(0,0,0,.18)}
.spread__left{left:14px;top:0;width:118px;height:884px;background:linear-gradient(90deg,#efece5,#f8f6f1 70%,#d9d3c7)}
.spread__spine{left:128px;top:0;width:10px;height:884px;background:linear-gradient(90deg,rgba(0,0,0,.14),rgba(0,0,0,0))}
.spine-title{left:42px;top:150px;writing-mode:vertical-rl;font-family:"Oswald",sans-serif;font-size:11px;letter-spacing:3px;color:var(--ink-soft)}

/* header */
.lead{left:140px;width:530px;top:18px;text-align:center;font-size:10px;color:var(--ink-soft)}
.kicker{left:380px;top:38px;font-family:"Noto Serif JP",serif;font-size:13px;color:var(--green)}
.headline{left:140px;width:530px;top:52px;text-align:center;font-family:"Noto Serif JP",serif;font-weight:700;font-size:42px;letter-spacing:2px;white-space:nowrap}
.headline-2{left:140px;width:530px;top:106px;text-align:center;font-family:"Noto Serif JP",serif;font-weight:700;font-size:36px;white-space:nowrap}
.tag{display:inline-block;background:var(--orange);color:var(--white);font-size:24px;padding:2px 8px;margin-right:6px;vertical-align:4px}
.sub{left:140px;width:530px;top:156px;text-align:center;font-size:11px;color:var(--ink-soft)}

/* photo mosaic */
.mosaic{left:150px;top:180px;width:512px;height:284px;display:grid;grid-template-columns:repeat(7,1fr);grid-template-rows:repeat(4,1fr);gap:6px}
.photo{background:linear-gradient(135deg,var(--stone),var(--leaf))}
.photo:nth-child(3n){background:linear-gradient(135deg,#a89a86,var(--wood))}
.photo:nth-child(4n){background:linear-gradient(135deg,#c8c2b4,#8f9a7a)}
.badge{border-radius:50%;background:var(--white);display:flex;flex-direction:column;align-items:center;justify-content:center;text-align:center;font-family:"Noto Serif JP",serif;font-weight:600;color:var(--ink);box-shadow:0 2px 6px rgba(0,0,0,.2)}
.badge small{font-size:11px;font-weight:400;color:var(--ink-soft)}
.badge b{font-size:26px;color:var(--orange)}
.badge--pages{left:150px;top:188px;width:94px;height:94px}
.badge--rare{left:560px;top:200px;width:94px;height:94px;font-size:13px}
.badge--free{left:360px;top:300px;width:90px;height:90px}
.badge--price{left:190px;top:360px;width:84px;height:84px;font-size:15px}

/* offer box */
.offer{left:214px;top:478px;width:446px;height:150px;background:var(--white);box-shadow:0 3px 10px rgba(0,0,0,.18)}
.offer__book{left:226px;top:492px;width:110px;height:90px;background:linear-gradient(135deg,#3a3632,#7c8a64);transform:skewY(-6deg)}
.offer__kicker{left:360px;top:494px;width:290px;text-align:right;font-size:11px;color:var(--green);font-family:"Noto Serif JP",serif}
.offer__title{left:360px;top:508px;width:290px;text-align:right;font-family:"Noto Serif JP",serif;font-weight:700;font-size:26px;white-space:nowrap}
.offer__title-2{left:360px;top:542px;width:290px;text-align:right;font-family:"Noto Serif JP",serif;font-weight:700;font-size:24px;white-space:nowrap}
.offer__title-2 .tag{font-size:16px}
.cta{left:246px;top:596px;width:384px;height:24px;background:var(--orange);border-radius:3px;color:var(--white);font-size:12px;font-weight:500;text-align:center;line-height:24px}

/* dark band */
.band{left:14px;top:640px;width:656px;height:236px;background:var(--band)}
.band__low{left:14px;top:790px;width:656px;height:86px;background:var(--band-low)}
.band__title{left:150px;top:650px;font-family:"Oswald",sans-serif;font-size:31px;line-height:36px;color:var(--white);letter-spacing:2px}
.thumbs{left:300px;top:654px;width:360px;height:78px;display:grid;grid-template-columns:repeat(8,1fr);grid-template-rows:repeat(2,1fr);gap:4px}
.band__text{left:300px;top:740px;width:360px;font-size:9px;line-height:14px;color:#d8d2c8}
.band__text.small{top:796px;color:#cfc8bd}
.band__photos{left:300px;top:818px;width:360px;height:50px;display:grid;grid-template-columns:repeat(7,1fr);gap:4px}

/* footer */
.blog{left:20px;top:902px;width:300px}
.blog__head{background:var(--green);color:var(--white);font-size:11px;padding:3px 6px}
.blog__list{list-style:none;font-size:10px;line-height:22px;color:var(--link);padding:2px 6px}
.blog__list li{border-bottom:1px dotted #bbb}
.side{left:332px;top:902px;width:100px}
.side__box{height:26px;background:#d6d1c8;margin-bottom:6px}
.side__box.green{background:#a9c08a;height:50px}
.social{left:440px;top:902px;width:72px;height:110px;background:#f4f2ee;border:1px solid #ccc}
.social__faces{left:446px;top:930px;width:60px;height:76px;background:linear-gradient(135deg,#c9bfb0,#8c8276)}
.brand{left:524px;top:944px;width:146px;text-align:center;font-family:"Noto Sans JP",sans-serif;font-weight:700;font-size:22px;color:var(--ink);white-space:nowrap}
.contact{left:520px;top:1000px;width:150px;text-align:right}
.contact__tel{font-size:18px;font-weight:700;display:flex;align-items:center;justify-content:flex-end;gap:4px}
.contact__mail{font-size:11px;color:var(--ink-soft);margin-top:4px}
</style>
</head>
<body>
<div class="abs spread"></div>
<div class="abs spread__left"></div>
<div class="abs spread__spine"></div>
<p class="abs spine-title">GARDEN AND EXTERIOR CATALOG</p>

<p class="abs lead">あなたのイメージする理想のエクステリアをお手元にお届けします！</p>
<p class="abs kicker">エクステリア &amp; ガーデン</p>
<h1 class="abs headline">施工事例カタログ</h1>
<p class="abs headline-2"><span class="tag">数量限定</span>プレゼント</p>
<p class="abs sub">制作費が非常に高いため、在庫が無くなり次第終了です</p>

<div class="abs mosaic" role="img" aria-label="エクステリア施工事例の写真一覧">
  <div class="photo"></div><div class="photo"></div><div class="photo"></div><div class="photo"></div><div class="photo"></div><div class="photo"></div><div class="photo"></div>
  <div class="photo"></div><div class="photo"></div><div class="photo"></div><div class="photo"></div><div class="photo"></div><div class="photo"></div><div class="photo"></div>
  <div class="photo"></div><div class="photo"></div><div class="photo"></div><div class="photo"></div><div class="photo"></div><div class="photo"></div><div class="photo"></div>
  <div class="photo"></div><div class="photo"></div><div class="photo"></div><div class="photo"></div><div class="photo"></div><div class="photo"></div><div class="photo"></div>
</div>
<div class="abs badge badge--pages"><small>フルカラー</small><b>300</b><small>ページ</small></div>
<div class="abs badge badge--rare"><small>エクステリアの</small>施工例に<br>特化</div>
<div class="abs badge badge--free"><small>定価1,890円が</small><b>無料</b></div>
<div class="abs badge badge--price">価格<br>掲載</div>

<div class="abs offer"></div>
<div class="abs offer__book" role="img" aria-label="施工事例カタログの表紙"></div>
<p class="abs offer__kicker">エクステリア &amp; ガーデン</p>
<p class="abs offer__title">施工事例カタログ</p>
<p class="abs offer__title-2"><span class="tag">数量限定</span>プレゼント</p>
<div class="abs cta">カタログ無料プレゼントへのお申し込み ▶</div>

<div class="abs band"></div>
<div class="abs band__low"></div>
<h2 class="abs band__title">GARDEN<br>AND<br>EXTERIOR<br>CATALOG</h2>
<div class="abs thumbs" role="img" aria-label="カタログ誌面の見本写真">
  <div class="photo"></div><div class="photo"></div><div class="photo"></div><div class="photo"></div><div class="photo"></div><div class="photo"></div><div class="photo"></div><div class="photo"></div>
  <div class="photo"></div><div class="photo"></div><div class="photo"></div><div class="photo"></div><div class="photo"></div><div class="photo"></div><div class="photo"></div><div class="photo"></div>
</div>
<p class="abs band__text">豊富な施工例をフルカラーで掲載した一冊。門まわり、駐車場、ウッドデッキ、植栽まで、実際の施工写真と価格を合わせてご覧いただけます。ご自宅の工事を考える際の金額の目安にお役立てください。</p>
<p class="abs band__text small">全国のお客様に無料でお届けしています。お早めにお申し込みください。</p>
<div class="abs band__photos" role="img" aria-label="施工例の写真">
  <div class="photo"></div><div class="photo"></div><div class="photo"></div><div class="photo"></div><div class="photo"></div><div class="photo"></div><div class="photo"></div>
</div>

<section class="abs blog">
  <h3 class="blog__head">ブログ新着記事</h3>
  <ul class="blog__list">
    <li>2014/05/12 新しい門まわりが完成しました</li>
    <li>2014/05/08 ウッドデッキの施工事例</li>
    <li>2014/04/30 春の植栽の手入れについて</li>
    <li>2014/04/22 駐車場リフォームのご紹介</li>
    <li>2014/04/15 ガーデンライトの新商品</li>
    <li>2014/04/09 カタログをお届けしました</li>
    <li>2014/04/02 スタッフ日記 庭づくり</li>
  </ul>
</section>
<div class="abs side">
  <div class="side__box"></div>
  <div class="side__box"></div>
  <div class="side__box green"></div>
  <div class="side__box"></div>
</div>
<div class="abs social"></div>
<div class="abs social__faces" role="img" aria-label="ファンの一覧"></div>

<p class="abs brand">灯砂ガーデン</p>
<div class="abs contact">
  <p class="contact__tel"><svg width="16" height="16" viewBox="0 0 24 24" aria-hidden="true"><path fill="#2b2622" d="M6.6 10.8a15 15 0 0 0 6.6 6.6l2.2-2.2c.3-.3.7-.4 1-.2 1.1.4 2.3.6 3.6.6.6 0 1 .4 1 1V20c0 .6-.4 1-1 1A17 17 0 0 1 3 4c0-.6.4-1 1-1h3.5c.6 0 1 .4 1 1 0 1.3.2 2.5.6 3.6.1.3 0 .7-.2 1z"/></svg>0120-418-327</p>
  <p class="contact__mail">info@tomosa-garden.com</p>
</div>
</body>
</html>
```